Elevated Playful Design needed for New York Paving Contractor

Every year, our company gives our customers fun gifts like stickers & car air fresheners, etc. This year, we'd like to elevate our gift with a playful design that promotes our brand & company vision.
We are looking for three designs incorporating our logo/brand and heavy equipment such as excavator, skid steer, and dump truck (see attached photos).
Each one would be used separately on its own sticker or car air freshener.
We like the color orange and please be as creative as possible.
The final design should promote our brand & make our customers feel happy & confident in their partnership with us.
For more info on our brand/ company, please visit: www.BrightHollow.com

```html
<!DOCTYPE html>
<html lang="en">
<head>
<meta charset="utf-8">
<title>Bright Hollow – Pavement Specialist Sticker</title>
<link href="https://fonts.googleapis.com/css2?family=Russo+One&display=swap" rel="stylesheet">
<style>
  :root {
    --bg: #e4e4e4;
    --frame: #f3f3f3;
    --card: #2d2c2c;
    --card-glow: #4a4340;
    --orange: #f58a3c;
    --orange-deep: #e2702a;
    --steel: #6a6a6a;
  }
  html, body {
    margin: 0;
    width: 826px;
    height: 1200px;
    overflow: hidden;
    background: var(--bg);
  }
  .sticker {
    position: relative;
    width: 826px;
    height: 1200px;
    font-family: "Russo One", sans-serif;
  }
  .sticker-card {
    position: absolute;
    left: 60px; top: 44px;
    width: 706px; height: 1112px;
    border-radius: 60px;
    background: radial-gradient(ellipse at 50% 70%, var(--card-glow) 0%, var(--card) 60%);
    box-shadow: 0 0 0 6px var(--frame);
  }
  .sticker-border {
    position: absolute;
    inset: 16px;
    border: 12px solid var(--orange);
    border-radius: 46px;
  }
  .machine-illustration {
    position: absolute;
    left: 150px; top: 140px;
    width: 550px; height: 350px;
    border-radius: 28px;
    background: linear-gradient(160deg, var(--orange) 0%, var(--orange-deep) 55%, var(--steel) 100%);
  }
  .tagline-arc {
    position: absolute;
    left: 0; top: 0;
    width: 826px; height: 1200px;
  }
  .tagline-arc text {
    font-family: "Russo One", sans-serif;
    font-size: 46px;
    fill: var(--orange);
    letter-spacing: 2px;
  }
  .brand-name {
    position: absolute;
    left: 0; right: 0;
    top: 800px;
    margin: 0;
    text-align: center;
    color: var(--orange);
    font-size: 92px;
    line-height: 96px;
    font-weight: 400;
  }
  .services {
    position: absolute;
    left: 0; right: 0;
    top: 1002px;
    margin: 0;
    text-align: center;
    color: var(--orange);
    font-size: 34px;
    letter-spacing: 1px;
  }
  .web-address {
    position: absolute;
    left: 0; right: 0;
    top: 1056px;
    margin: 0;
    text-align: center;
    color: var(--orange);
    font-size: 20px;
    letter-spacing: 6px;
  }
</style>
</head>
<body>
  <main class="sticker">
    <div class="sticker-card">
      <div class="sticker-border"></div>
    </div>

    <div class="machine-illustration" role="img" aria-label="Orange skid steer loader illustration with the company web address on its lift arm"></div>

    <svg class="tagline-arc" viewBox="0 0 826 1200" aria-hidden="false">
      <defs>
        <path id="tagline-curve" d="M 130 780 Q 413 560 696 780" fill="none"/>
      </defs>
      <text text-anchor="middle">
        <textPath href="#tagline-curve" startOffset="50%">PAVEMENT SPECIALIST</textPath>
      </text>
    </svg>

    <h1 class="brand-name">BRIGHT<br>HOLLOW</h1>
    <p class="services">ASPHALT &amp; CONCRETE</p>
    <p class="web-address">WWW.BRIGHTHOLLOW.COM</p>
  </main>
</body>
</html>
```